Flyer Design Project - Financial services business specialising in mortgages and insurance

I require a flyer to create interest in saving money with mortgages. We show people that they can save money on their mortgages by paying the mortgage of sooner. Therefore they no longer need to work for the bank, and that they can live their life debt free.
The call to action is that they pick up the phone and call me or make an inquiry online via our website.

We are a insurance and mortgage brokerage and the business name is called BRAVO. Website: www.bravolenders.co.nz (currently)
the new website that isn't quite live yet is viewable at
www.qortesite.com/bravo

Our tag line is Home Hope Horizon

The type of clients we are trying to engage with are home owners with existing mortgages.

Aged between 35-40, Professionals, Income bracket of $80k plus for the household, in a relationship, no more than two kids, live in our local area (West Auckland, New Zealand) they are driven to be successful and have a comfortable family life and be able to afford luxuries.(responsible)

We would like to see what options someone can come up other than the ususal. Needs to fit with our business name BRAVO + Tag line. As in we do things BRAVOER.

The flyer needs to show that we can help make a difference.

We will provide a free comparative market report on their house for an appointment and also if we cant save the prospect any money our guarantee is that we will give them a $20 voucher. (conditions will apply).

Ideally looking to have the flyer on a DLE size although we are open to options.

more than happy to discuss further if required to. I have attached my logo and my current image for home loans used on the website although i would like to see if there are any better options available than my current image.

Target Market(s)

home owners with an existing mortgage. Ages between 35-40, Professionals, Income 80k+

Industry/Entity Type

Insurance

Requirements
Must have
• A disclosure document is available upon request.
Our logo and contact details.
Call to action
Nice to have
• Want to focus on the lifestyles and goals rather than the actual payment of the mortgage.
Should not have
• We don't want to be saying the same boring message as most mortgage brokers are saying ie. Call us we can save you thousands of dollars.
We a need a reason for them to call us to go with our image and brand.

```html
<!DOCTYPE html>
<html lang="en">
<head>
<meta charset="utf-8">
<title>Bravo – Your Family Life Free of Debt</title>
<link rel="stylesheet" href="https://fonts.googleapis.com/css2?family=Roboto:wght@300;400&display=swap">
<style>
  :root {
    --brand-blue: #1075c2;
    --brand-navy: #1d4f8c;
    --ink: #101820;
    --muted: #5a6470;
    --paper: #ffffff;
    --photo-sky: #cfe3f3;
    --photo-warm: #d8b79a;
    --photo-shirt: #9aa3ab;
  }
  * { margin: 0; padding: 0; box-sizing: border-box; }
  html, body { width: 1200px; height: 601px; overflow: hidden; background: var(--paper); }
  .flyer {
    position: relative;
    width: 1200px;
    height: 601px;
    background: var(--paper);
    font-family: "Roboto", "Helvetica Neue", Arial, sans-serif;
    font-weight: 300;
  }
  .family-photo {
    position: absolute;
    left: 0; top: 0;
    width: 692px; height: 601px;
    background:
      radial-gradient(ellipse 60% 55% at 45% 55%, var(--photo-warm) 0%, rgba(216,183,154,0.5) 55%, transparent 80%),
      linear-gradient(180deg, var(--photo-sky) 0%, #e6eef5 50%, var(--photo-shirt) 100%);
  }
  .brand {
    position: absolute;
    left: 810px; top: 20px;
    width: 240px;
    text-align: center;
    color: var(--brand-blue);
  }
  .brand-name {
    font-size: 80px;
    font-weight: 400;
    line-height: 1;
    letter-spacing: -1px;
  }
  .brand-tagline {
    margin-top: 4px;
    font-size: 18px;
    font-weight: 400;
    color: var(--brand-navy);
  }
  .offer-panel {
    position: absolute;
    left: 692px; top: 171px;
    width: 476px; height: 403px;
    background: var(--brand-blue);
    border-radius: 0 16px 16px 0;
    padding: 22px 10px 0 43px;
    color: var(--paper);
  }
  .offer-kicker { font-size: 25px; line-height: 1.1; white-space: nowrap; }
  .offer-headline {
    margin-top: 6px;
    font-size: 56px;
    font-weight: 300;
    line-height: 1;
  }
  .offer-body {
    margin-top: 16px;
    font-size: 15.5px;
    line-height: 1.24;
    white-space: nowrap;
  }
  .offer-body p + p { margin-top: 17px; }
  .call-to-action .phone,
  .call-to-action .web { color: var(--ink); }
  .disclosure {
    position: absolute;
    left: 735px; top: 581px;
    font-size: 11px;
    font-weight: 400;
    color: var(--muted);
  }
</style>
</head>
<body>
  <main class="flyer">
    <div class="family-photo" role="img" aria-label="Smiling family of four, parents carrying two young children on their backs, against a bright sky"></div>

    <header class="brand">
      <div class="brand-name">Bravo</div>
      <div class="brand-tagline">Home Hope Horizon</div>
    </header>

    <section class="offer-panel">
      <p class="offer-kicker">We Can Make a Difference by Helping</p>
      <h1 class="offer-headline">Your Family Life<br>Free of Debt</h1>
      <div class="offer-body">
        <p>There are many ways to keep your family safe and happy,<br>but a bank loan is not the way to make it happen.</p>
        <p>We found a different way to save money on your<br>mortgage. We’ll give you a free comparative market<br>report on your house for an appointment, and if we<br>can’t save you any money, we’ll give you a $20 voucher,<br>guaranteed. (Conditions apply.)</p>
        <p class="call-to-action">Call us on: <span class="phone">09 555 0147</span> or make an inquiry online at<br><span class="web">www.bravolenders.co.nz</span> for a bravoer solution.</p>
      </div>
    </section>

    <p class="disclosure">A disclosure document is available upon request.</p>
  </main>
</body>
</html>
```